Marketing folder with booklet and brochure. Slot for business card

We are a dual-branded commercial and residential flooring installation company. Carpet, resilient, wood, tile, flooring repairs, sand and finish wood. We like designs using red, white, and blue. Custom Font style is Luna Bar, available upon request Content available on our website obrinworks.com. Ideally would like a small booklet of services, letterhead for intro letter, folder, and possibly tri-fold.

Target Market(s)

Builders, designers, and contractors. We do not typically work for the general public

Industry/Entity Type

Construction

Contact Information for Business Card

We currently have business cards, but because we want a card slot in the folder, we might have to match toward our print package. Check out our web site obrinworks.com

Font styles to use
Serif

Colors
0456a4
ec1f27
ffffff

```html
<!DOCTYPE html>
<html lang="en">
<head>
<meta charset="utf-8">
<title>Obrin Works – Our Services</title>
<link rel="stylesheet" href="https://fonts.googleapis.com/css2?family=Questrial&display=swap">
<style>
  :root {
    --brand-red: #ec1f27;
    --deep-red: #c4161d;
    --dark-red: #a91218;
    --brand-blue: #0456a4;
    --white: #ffffff;
    --title-tint: rgba(255, 255, 255, 0.62);
    --wood-light: #ecd3ad;
    --wood-mid: #d9b483;
    --wood-dark: #b98a58;
  }
  html, body {
    margin: 0;
    padding: 0;
    width: 846px;
    height: 1200px;
    overflow: hidden;
    background: var(--white);
  }
  .cover {
    position: relative;
    width: 846px;
    height: 1200px;
    overflow: hidden;
    font-family: "Questrial", "Century Gothic", sans-serif;
  }
  .cover-art {
    position: absolute;
    inset: 0;
    width: 846px;
    height: 1200px;
  }
  .brand-name {
    position: absolute;
    top: 192px;
    left: 0;
    width: 1020px;
    margin: 0;
    text-align: center;
    font-size: 64px;
    font-weight: 400;
    letter-spacing: 1px;
    color: var(--brand-blue);
  }
  .tagline {
    position: absolute;
    top: 296px;
    left: 0;
    width: 1086px;
    margin: 0;
    text-align: center;
    font-size: 31px;
    color: var(--white);
  }
  .page-title {
    position: absolute;
    top: 468px;
    left: 0;
    width: 936px;
    margin: 0;
    text-align: center;
    font-size: 96px;
    font-weight: 400;
    letter-spacing: 1px;
    color: var(--title-tint);
  }
  .division-mark {
    position: absolute;
    left: 510px;
    top: 1098px;
    display: flex;
    align-items: center;
    gap: 10px;
    color: var(--brand-blue);
    font-size: 24px;
    line-height: 1.05;
  }
  .division-mark .mark-square {
    width: 30px;
    height: 30px;
    background: var(--brand-blue);
  }
</style>
</head>
<body>
  <main class="cover">
    <svg class="cover-art" viewBox="0 0 846 1200" xmlns="http://www.w3.org/2000/svg">
      <defs>
        <radialGradient id="redGlow" cx="0.72" cy="0.35" r="0.75">
          <stop offset="0" stop-color="#ee2a30"/>
          <stop offset="1" stop-color="#e01c24"/>
        </radialGradient>
        <linearGradient id="woodTone" x1="0" y1="0" x2="1" y2="1">
          <stop offset="0" stop-color="#f4ead9"/>
          <stop offset="0.3" stop-color="var(--wood-light)"/>
          <stop offset="0.65" stop-color="var(--wood-mid)"/>
          <stop offset="1" stop-color="var(--wood-dark)"/>
        </linearGradient>
      </defs>
      <rect class="red-field" width="846" height="1200" fill="url(#redGlow)"/>
      <path class="red-sweep" d="M0,0 H420 C250,80 120,260 110,520 L0,560 Z" fill="var(--deep-red)" opacity="0.55"/>
      <path class="red-sweep-inner" d="M0,0 H220 C120,90 40,220 0,320 Z" fill="var(--dark-red)" opacity="0.45"/>
      <path class="white-wave" d="M0,680 C60,625 180,600 330,650 C520,715 700,830 846,880 V1200 H0 Z" fill="var(--white)"/>
      <path class="photo-area" role="img" aria-label="Photo of a flooring installer laying light oak laminate planks, with a tape measure, hammer and wood offcuts in the foreground"
            d="M0,760 C160,715 330,730 500,790 C640,840 760,890 846,905 V1200 H0 Z" fill="url(#woodTone)"/>
    </svg>

    <h1 class="brand-name">Obrin Works</h1>
    <p class="tagline">Floor and More</p>
    <h2 class="page-title">Our Services</h2>

    <div class="division-mark">
      <span class="mark-square"></span>
      <span class="mark-name">OBRIN<br>COMMERCIAL FLOORING</span>
    </div>
  </main>
</body>
</html>
```